QR TILL WORKS , CREDIT CARD PROCESSING EQUIPMENT

qrtillworks is a sub division of Tallow a credit car processing co.
dorian vell
14 cedar hollow ln
Quillmere QM 07312
suite 412

qrtillworks.example
cell 555-214-7730
office 555-861-2093
we sell pos systems to merchant who want to accept credit cards at there retail location.
black card would be nice buit open to different ideas

Target Market(s)

retail merchants

Industry/Entity Type

credit card processing

Contact Information for Business Card

card should include web site phone address

Colors

Designer to choose colors to be used in the design.

Requirements
Should not have
• red

```html
<!DOCTYPE html>
<html lang="en">
<head>
<meta charset="utf-8">
<title>QR Till Works — Business Card</title>
<link href="https://fonts.googleapis.com/css2?family=Rubik:wght@500;700&display=swap" rel="stylesheet">
<style>
  :root {
    --backdrop: #a9a9a9;
    --card-black: #070707;
    --card-yellow: #e9c21a;
    --ink-white: #ffffff;
  }
  * { margin: 0; padding: 0; box-sizing: border-box; }
  html, body { width: 1127px; height: 1200px; overflow: hidden; }
  body {
    position: relative;
    background: var(--backdrop);
    font-family: "Rubik", Arial, sans-serif;
    color: var(--ink-white);
  }
  .card {
    position: absolute;
    left: 324px;
    width: 514px;
    height: 296px;
  }
  .card-front { top: 264px; background: var(--card-black); }
  .card-back { top: 642px; background: var(--card-yellow); }

  .wordmark {
    position: absolute;
    inset: 0;
    display: flex;
    align-items: center;
    justify-content: center;
    gap: 14px;
  }
  .wordmark-dot {
    width: 22px; height: 22px;
    border-radius: 50%;
    background: var(--card-yellow);
  }
  .wordmark-name {
    font-weight: 500;
    font-size: 38px;
    letter-spacing: 1px;
    color: var(--ink-white);
  }

  .person-name {
    position: absolute;
    left: 42px; top: 42px;
    font-weight: 700;
    font-size: 32px;
    line-height: 39px;
  }
  .contact-line {
    position: absolute;
    left: 280px;
    display: flex;
    align-items: center;
    gap: 10px;
    font-weight: 500;
    font-size: 16px;
    letter-spacing: 2px;
  }
  .contact-line svg { flex: none; }
  .phone-cell { top: 54px; }
  .phone-office { top: 86px; }
  .address {
    position: absolute;
    left: 280px; top: 206px;
    display: flex;
    align-items: flex-start;
    gap: 10px;
  }
  .address-lines {
    font-style: normal;
    font-weight: 500;
    font-size: 14px;
    line-height: 19px;
    letter-spacing: 1px;
  }
  .website {
    position: absolute;
    left: 42px; top: 234px;
    padding: 2px 7px;
    background: var(--ink-white);
    color: var(--card-yellow);
    font-weight: 500;
    font-size: 14px;
    letter-spacing: 0.5px;
  }
</style>
</head>
<body>
  <section class="card card-front" aria-label="Card front">
    <div class="wordmark">
      <span class="wordmark-dot"></span>
      <span class="wordmark-name">QR TILL WORKS</span>
    </div>
  </section>

  <section class="card card-back" aria-label="Card back">
    <h1 class="person-name">Dorian<br>Vell</h1>

    <div class="contact-line phone-cell">
      <svg width="24" height="24" viewBox="0 0 24 24" aria-hidden="true">
        <circle cx="12" cy="12" r="12" fill="#fff"/>
        <rect x="8" y="5" width="8" height="14" rx="1.5" fill="none" stroke="#e9c21a" stroke-width="1.6"/>
        <rect x="10" y="16" width="4" height="1.2" fill="#e9c21a"/>
      </svg>
      <span>555-214-7730</span>
    </div>

    <div class="contact-line phone-office">
      <svg width="24" height="24" viewBox="0 0 24 24" aria-hidden="true">
        <circle cx="12" cy="12" r="12" fill="#fff"/>
        <path d="M6 10c0-2 3-3 6-3s6 1 6 3v1h-3v-1.5h-6V11H6z" fill="#e9c21a"/>
        <rect x="7.5" y="12" width="9" height="5" rx="1" fill="#e9c21a"/>
      </svg>
      <span>555-861-2093</span>
    </div>

    <div class="address">
      <svg width="24" height="24" viewBox="0 0 24 24" aria-hidden="true">
        <circle cx="12" cy="12" r="12" fill="#fff"/>
        <path d="M12 5a5 5 0 0 0-5 5c0 3.5 5 9 5 9s5-5.5 5-9a5 5 0 0 0-5-5z" fill="#e9c21a"/>
        <circle cx="12" cy="10" r="2" fill="#fff"/>
      </svg>
      <address class="address-lines">
        14 Cedar Hollow Ln<br>
        Quillmere QM 07312<br>
        Suite 412
      </address>
    </div>

    <div class="website">QRTILLWORKS.EXAMPLE</div>
  </section>
</body>
</html>
```